Product Description page for Hullwrap.com, References here just need a clean up redesign

Hi, were working on updating the product description page of our site hullwrap.com

Attached is a reference of what we drew on paint. We want to keep it pretty much the same as far as whats on there, the components with a few small adjustments and a clean actually designed look.

1. We want to remove the tabs (product description, warranty, reviews) and put it all in that main content area stretching down into sections. IE: Product Description section, followed by reviews, followed by warranty, below each other.
2. The side bar needs to be redesigned as far as the look and feel but the content and whats in there should stay the same.
3. The main banner area will be replaced shortly you do not have to worry about that.
4. Include a section or box for people to put in their email for a free Ebook.

Target Market(s)

people looking to easily view our boat cover products and buy without having to click too often or leave the page.

Industry/Entity Type

Online Shopping

Number of Pages Required

1 page

Requirements
Must have
• - Must update the sidebar
• - Must update the content area to remove the tabs and put the content from each tab sectioned off below each other (dummy text is fine for now for the tabs you cant view)
Nice to have
• - Cool place thats clean and functional to insert a section for people to put in their email to receive a free ebook
Should not have
• - too much change, we already know what we want and have a solid reference to work from.

```html
<!DOCTYPE html>
<html lang="en">
<head>
<meta charset="utf-8">
<title>Up to 16'8" Long and 90" Wide – Hullwrap.com</title>
<link href="https://fonts.googleapis.com/css2?family=Lato:wght@400;700;900&display=swap" rel="stylesheet">
<style>
:root{
  --brand-blue:#2457c9;
  --link-blue:#2f7fd8;
  --ink:#222;
  --muted:#555;
  --line:#e3e3e3;
  --panel:#f5f5f5;
  --page:#ffffff;
  --price-red:#e3262d;
  --cta-orange:#f58a22;
  --ebook-green:#2e9a3a;
  --star:#f2b705;
  --tick:#3aa64a;
}
*{box-sizing:border-box;margin:0;padding:0}
html,body{width:1200px;height:2706px;overflow:hidden;background:var(--page)}
body{font-family:'Lato',Arial,sans-serif;color:var(--ink);position:relative}
.abs{position:absolute}
.site-header{left:0;top:0;width:1200px;height:81px;background:var(--brand-blue);color:#fff;font-weight:900;font-size:34px;padding:18px 0 0 68px}
.breadcrumb{left:68px;top:97px;font-size:17px;color:#444}
.breadcrumb span{margin:0 8px;color:#888}
.breadcrumb b{color:var(--brand-blue)}
.page-frame{left:68px;top:135px;width:1064px;height:2493px;border:2px solid var(--line)}
.fits-bar{left:90px;top:149px;width:1020px;height:68px;background:var(--panel);font-size:17px;padding:22px 0 0 24px;color:#444}
.fits-bar b{color:var(--ink)}
.hero-photo{left:90px;top:232px;width:695px;height:362px;background:linear-gradient(180deg,#fafafa 0%,#dcdde0 55%,#b9bcc2 100%)}
.thumb-row{left:108px;top:610px;display:flex;gap:10px}
.thumb{width:87px;height:92px;background:linear-gradient(160deg,#6b7686,#2c333d);border:2px solid #ddd}
.thumb.blue{background:linear-gradient(160deg,#3d82c8,#1a4c86)}
.thumb.grey{background:linear-gradient(160deg,#c9ccd2,#7d828a)}
.buy-box{left:794px;top:528px;width:311px;height:569px;background:#fff;box-shadow:0 6px 16px rgba(0,0,0,.22);padding:24px 26px}
.price{color:var(--price-red);font-size:38px;font-weight:900}
.kv{display:flex;justify-content:space-between;font-size:16px;color:#333;line-height:27px}
.kv.gap{margin-top:14px}
.field{display:flex;justify-content:space-between;align-items:center;margin-top:22px;font-size:16px;font-weight:700}
.select{width:150px;height:38px;border:1px solid #ddd;font-weight:400;font-size:15px;display:flex;align-items:center;justify-content:space-between;padding:0 12px}
.small-select{width:80px}
.required{color:var(--price-red);font-size:14px;text-align:right;margin-top:6px}
.add-cart{margin-top:24px;height:72px;background:var(--cta-orange);color:#fff;font-weight:900;font-size:25px;display:flex;align-items:center;justify-content:center;border-radius:3px}
.free-ship{margin-top:20px;display:flex;align-items:center;justify-content:center;gap:10px;font-weight:700;font-size:17px;color:var(--brand-blue)}
.card{left:90px;width:668px;background:#fff;box-shadow:0 2px 10px rgba(0,0,0,.13);padding:26px 32px}
.card h2{color:var(--link-blue);font-size:28px;font-weight:900;margin-bottom:16px;display:flex;justify-content:space-between}
.card h2 svg{margin-top:4px}
.card p{font-size:15.5px;line-height:22px;color:#333}
.card h3{font-size:16px;font-weight:900;margin-bottom:4px}
.features{list-style:none;margin-top:6px}
.features li{font-size:15.5px;line-height:33px;color:#333;display:flex;gap:12px;align-items:flex-start}
.features li svg{margin-top:11px;flex:none}
.features li.wrap{line-height:24px;padding:5px 0}
.features li.wrap svg{margin-top:5px}
.review{margin-bottom:22px}
.stars{display:flex;gap:2px;margin-bottom:6px}
.review .who{color:var(--link-blue);font-style:italic;font-size:15px;margin-top:6px}
.link{color:var(--link-blue)}
.delivery{background:var(--panel);height:56px;display:flex;align-items:center;gap:14px;padding-left:14px;font-weight:700;font-size:16px;margin:4px 0 18px}
.spec{display:flex;font-size:16px;line-height:40px}
.spec span:first-child{width:140px}
.side-title{left:807px;top:1118px;font-size:18px;font-weight:900;display:flex;flex-direction:column;gap:4px}
.addon{left:807px;width:300px;display:flex;gap:20px}
.addon-photo{width:70px;height:96px;flex:none;background:linear-gradient(160deg,#555,#111);border-radius:4px}
.addon-photo.pole{width:50px;margin:0 10px;background:linear-gradient(90deg,#bbb,#444)}
.addon-photo.motor{background:linear-gradient(160deg,#2966b8,#0f2f66)}
.addon-name{color:var(--link-blue);font-weight:900;font-size:17px;line-height:21px}
.addon-desc{font-size:15px;line-height:20px;color:#333}
.addon-free{color:var(--price-red);font-weight:900;font-size:15px}
.addon-price{color:var(--price-red);font-weight:900;font-size:19px;display:flex;align-items:center;gap:22px}
.promo{left:794px;top:1782px;width:311px;height:336px;background:#fff;box-shadow:0 4px 14px rgba(0,0,0,.2);text-align:center;padding-top:30px}
.promo .lead{font-size:21px;color:#333}
.promo .lead-2{font-size:22px;font-weight:900}
.promo-photo{width:180px;height:88px;margin:16px auto 10px;background:linear-gradient(180deg,#5ea9e6,#1d5a9a 70%,#777 100%);border-radius:40px 40px 6px 6px}
.promo-name{color:var(--link-blue);font-weight:900;font-size:15px;line-height:19px;padding:0 20px}
.was{color:#777;text-decoration:line-through;font-size:15px;margin-top:4px}
.now{color:var(--price-red);font-weight:900;font-size:22px}
.ebook{left:794px;top:2154px;width:311px;height:271px;background:#f2f2f2;box-shadow:0 4px 14px rgba(0,0,0,.2);padding:22px 20px}
.ebook-head{display:flex;justify-content:space-between}
.ebook-head .t1{font-size:25px;font-weight:900;line-height:28px}
.ebook-head .t2{font-size:32px;font-weight:900;line-height:34px}
.email{margin-top:14px;height:52px;background:#fff;display:flex;align-items:center;gap:12px;padding-left:14px;font-size:15px;color:#777;font-style:italic}
.ebook-btn{margin-top:12px;height:58px;background:var(--ebook-green);color:#fff;display:flex;align-items:center;justify-content:center;font-weight:900;font-size:24px;gap:6px}
.ebook-btn small{font-size:15px}
</style>
</head>
<body>
<header class="abs site-header">Up to 16'8" Long and 90" Wide</header>
<nav class="abs breadcrumb">Home<span>›</span>Boat Covers<span>›</span>Center console with Bow Rails<span>›</span><b>Up to 16'8" Long and 90" Wide</b></nav>

<div class="abs page-frame"></div>
<div class="abs fits-bar">✓ Fits: <b>Center Console with Bow Rails up to 16'8" Long and 90" Wide</b></div>
<div class="abs hero-photo" role="img" aria-label="Grey boat cover fitted on a center console boat on a trailer"></div>
<div class="abs thumb-row">
  <div class="thumb" role="img" aria-label="Product badge thumbnail"></div>
  <div class="thumb blue" role="img" aria-label="Fabric close-up thumbnail"></div>
  <div class="thumb" role="img" aria-label="Covered boat thumbnail"></div>
  <div class="thumb grey" role="img" aria-label="Strap detail thumbnail"></div>
  <div class="thumb" role="img" aria-label="Cover detail thumbnail"></div>
  <div class="thumb grey" role="img" aria-label="Accessories thumbnail"></div>
</div>

<aside class="abs buy-box">
  <div class="price">$331.50</div>
  <div class="kv"><span>Regular price:</span><span>$442.00</span></div>
  <div class="kv"><span>You Save:</span><span>$110.50</span></div>
  <div class="kv gap"><span>Availability:</span><span>Ready to Ship</span></div>
  <div class="kv"><span>Ships:</span><span>1 Business Day</span></div>
  <div class="field"><span>Color:</span><div class="select">Please Select <span>▾</span></div></div>
  <div class="required">*Required</div>
  <div class="field"><span>Quantity:</span><div class="select small-select">1 <span>▾</span></div></div>
  <div class="add-cart">ADD TO CART</div>
  <div class="free-ship">
    <svg width="40" height="40" viewBox="0 0 40 40"><circle cx="20" cy="20" r="18" fill="none" stroke="#2457c9" stroke-width="2"/><path d="M9 14h14v11H9zM23 18h5l3 4v3h-8z" fill="#2457c9"/><circle cx="13" cy="27" r="2.5" fill="#fff" stroke="#2457c9" stroke-width="1.5"/><circle cx="27" cy="27" r="2.5" fill="#fff" stroke="#2457c9" stroke-width="1.5"/></svg>
    Free Shipping*
  </div>
</aside>

<section class="abs card" style="top:745px;height:731px">
  <h2>Product Info <svg width="14" height="10"><path d="M1 9l6-7 6 7" fill="none" stroke="#ccc" stroke-width="2"/></svg></h2>
  <h3>Description:</h3>
  <p>When a boat is stored outside it is exposed to harmful elements sich as wind, dirt, rain, and UV. The Harbor Shield is the most powerful cover available providing 10x more strenght and protection compared to the competition. The 1200 denier fabric is 100% waterproof and provides excellent protection against sun, rain, wind and snow.</p>
  <h3 style="margin-top:20px">Features:</h3>
  <ul class="features">
    <li><svg width="14" height="12"><path d="M1 6l4 4 8-9" fill="none" stroke="#2f7fd8" stroke-width="2"/></svg>5 Star Fit. Fit guaranteed or your money back</li>
    <li><svg width="14" height="12"><path d="M1 6l4 4 8-9" fill="none" stroke="#2f7fd8" stroke-width="2"/></svg>10 Year Warranty. Full warranty covering rips and tears</li>
    <li><svg width="14" height="12"><path d="M1 6l4 4 8-9" fill="none" stroke="#2f7fd8" stroke-width="2"/></svg>The covers comes in Grey, Blue and Maroon</li>
    <li><svg width="14" height="12"><path d="M1 6l4 4 8-9" fill="none" stroke="#2f7fd8" stroke-width="2"/></svg>The fabric is pure 100% Marine Polyester (no cotton mix)</li>
    <li><svg width="14" height="12"><path d="M1 6l4 4 8-9" fill="none" stroke="#2f7fd8" stroke-width="2"/></svg>No worries, the cover won't stretch or shrink</li>
    <li><svg width="14" height="12"><path d="M1 6l4 4 8-9" fill="none" stroke="#2f7fd8" stroke-width="2"/></svg>Rain or sleet the cover is 100% waterproof</li>
    <li><svg width="14" height="12"><path d="M1 6l4 4 8-9" fill="none" stroke="#2f7fd8" stroke-width="2"/></svg>Fully Breathable, you'll never see mold or mildew</li>
    <li><svg width="14" height="12"><path d="M1 6l4 4 8-9" fill="none" stroke="#2f7fd8" stroke-width="2"/></svg>UV resistant and also prevents heat buildup</li>
    <li><svg width="14" height="12"><path d="M1 6l4 4 8-9" fill="none" stroke="#2f7fd8" stroke-width="2"/></svg>Fully Trailerable (straps included)</li>
    <li class="wrap"><svg width="14" height="12"><path d="M1 6l4 4 8-9" fill="none" stroke="#2f7fd8" stroke-width="2"/></svg><span>The cover also comes with an integrated hem cord to be used when mooring or on boat lifts</span></li>
    <li><svg width="14" height="12"><path d="M1 6l4 4 8-9" fill="none" stroke="#2f7fd8" stroke-width="2"/></svg>Tough-Strong-Durable</li>
  </ul>
</section>

<section class="abs card" style="top:1503px;height:339px">
  <h2>Reviews <svg width="14" height="10"><path d="M1 9l6-7 6 7" fill="none" stroke="#ccc" stroke-width="2"/></svg></h2>
  <div class="review">
    <div class="stars">
      <svg width="100" height="18" viewBox="0 0 100 18"><g fill="#f2b705"><path id="st" d="M9 1l2.4 5.2 5.6.6-4.2 3.8 1.2 5.6L9 13.4 4 16.2l1.2-5.6L1 6.8l5.6-.6z"/><use href="#st" x="20"/><use href="#st" x="40"/><use href="#st" x="60"/><use href="#st" x="80"/></g></svg>
    </div>
    <p>Great product! Totally satisfied, thank you for the support!</p>
    <div class="who">Tom Ray Hollis</div>
  </div>
  <div class="review">
    <div class="stars"><svg width="100" height="18" viewBox="0 0 100 18"><g fill="#f2b705"><use href="#st"/><use href="#st" x="20"/><use href="#st" x="40"/><use href="#st" x="60"/><use href="#st" x="80"/></g></svg></div>
    <p>Fast delivery and the cover with hight quality, I'm very happy with it.</p>
    <div class="who">Nina Crane M.</div>
  </div>
</section>

<section class="abs card" style="top:1856px;height:447px">
  <h2>Warranty <svg width="14" height="10"><path d="M1 9l6-7 6 7" fill="none" stroke="#ccc" stroke-width="2"/></svg></h2>
  <p>When a boat is stored outside it is exposed to harmful elements sich as wind, dirt, rain, and UV. The Harbor Shield is the most powerful cover available providing 10x more strenght and protection compared to the competition. The 1200 denier fabric is <span class="link">100% waterproof</span> and provides excellent protection against sun, rain, wind and snow. The Harbor Shield is the most powerful cover available providing 10x more <span class="link">strenght and protection</span> compared to the competition. The 1200 denier fabric is 100% waterproof and provides excellent protection against sun, rain, wind and snow.</p>
  <p style="margin-top:20px">The Harbor Shield is the most powerful cover available providing 10x more <span class="link">strenght and protection</span> compared to the competition. The 1200 denier fabric is 100% waterproof and provides excellent protection against sun, rain, wind and snow.</p>
</section>

<section class="abs card" style="top:2330px;height:270px">
  <h2>Shipping <svg width="14" height="10"><path d="M1 9l6-7 6 7" fill="none" stroke="#ccc" stroke-width="2"/></svg></h2>
  <div class="delivery">
    <svg width="32" height="32" viewBox="0 0 32 32"><circle cx="16" cy="16" r="14" fill="none" stroke="#2f7fd8" stroke-width="2"/><path d="M18 6l-7 11h5l-2 9 7-11h-5z" fill="#2f7fd8"/></svg>
    Estimated Delivery Delay: 1 day
  </div>
  <div class="spec"><span>Weight:</span><span>10kg</span></div>
  <div class="spec"><span>Dimensions:</span><span>4 x 2 m</span></div>
</section>

<div class="abs side-title">
  <svg width="34" height="26" viewBox="0 0 34 26"><rect x="2" y="8" width="22" height="16" fill="none" stroke="#2f7fd8" stroke-width="2"/><rect x="9" y="2" width="22" height="16" fill="#fff" stroke="#2f7fd8" stroke-width="2"/></svg>
  Frequently Purchased Together
</div>

<div class="abs addon" style="top:1214px">
  <div class="addon-photo pole" role="img" aria-label="Telescopic support pole"></div>
  <div><div class="addon-name">SUPPORT POLE</div><div class="addon-desc">Works for Boats and Trucks!</div><div class="addon-price">$30.75</div></div>
</div>
<div class="abs addon" style="top:1341px">
  <div class="addon-photo motor" role="img" aria-label="Blue outboard motor cover"></div>
  <div><div class="addon-name">BOAT MOTOR COVER</div><div class="addon-desc">Heavy duty waterproof material!</div><div class="addon-price">$43.06</div></div>
</div>
<div class="abs addon" style="top:1476px">
  <div class="addon-photo" role="img" aria-label="Coiled black straps with buckles"></div>
  <div><div class="addon-name">132 IN STRAPS AND BUCKLE PACK</div><div class="addon-free">FREE!</div><div class="addon-price">$26.14 <svg width="30" height="26"><path d="M2 14l9 9L28 2" fill="none" stroke="#3aa64a" stroke-width="3"/></svg></div></div>
</div>
<div class="abs addon" style="top:1630px">
  <div class="addon-photo" role="img" aria-label="Black storage bag"></div>
  <div><div class="addon-name">STORAGE BAG</div><div class="addon-free">FREE!</div><div class="addon-price">$26.14 <svg width="30" height="26"><path d="M2 14l9 9L28 2" fill="none" stroke="#3aa64a" stroke-width="3"/></svg></div></div>
</div>

<aside class="abs promo">
  <div class="lead">Looking for an</div>
  <svg width="220" height="14" viewBox="0 0 220 14"><path d="M4 12Q110 -4 216 12" fill="none" stroke="#f58a22" stroke-width="2"/></svg>
  <div class="lead-2">indoor cover?</div>
  <div class="promo-photo" role="img" aria-label="Blue boat cover on a runabout on a trailer"></div>
  <div class="promo-name">Keelmark 600 Denier Boat Cover fits V-Hull Runabout</div>
  <div class="was">$300.00</div>
  <div class="now">$138.81</div>
</aside>

<aside class="abs ebook">
  <div class="ebook-head">
    <div><div class="t1">Sign Up for</div><div class="t2">a free Ebook</div></div>
    <svg width="56" height="46" viewBox="0 0 56 46"><path d="M28 10C20 4 10 4 3 6v34c7-2 17-2 25 4 8-6 18-6 25-4V6c-7-2-17-2-25 4zM28 10v34" fill="#fff" stroke="#2f7fd8" stroke-width="2.5"/></svg>
  </div>
  <div class="email">
    <svg width="22" height="16" viewBox="0 0 22 16"><rect x="1" y="1" width="20" height="14" fill="none" stroke="#333" stroke-width="1.6"/><path d="M1 1l10 8 10-8" fill="none" stroke="#333" stroke-width="1.6"/></svg>
    Enter your email
  </div>
  <div class="ebook-btn">Get E-Book <small>(FREE)</small></div>
</aside>
</body>
</html>
```